Frozen Yoghurt Flyer Design Project

Hello, we are looking for a flyer design for a frozen yoghurt shop competition called 'Best Glacio' (Glacio is the shop name). This competition rule is simply post your yoghurt creation on Glacio Chatterbox and tag #bestglacio, who's frozen yoghurt gets the most vote win the game(for more details tell people please check Glacio Chatterbox). The total prize is up to $2,500, and they will also get a chance to win an Tabula2 with custom Glacio vinyl cover.
We would like to see designs that use the colors black, white and pink. The final design should focus on attract school students, teenagers, college girls, and encourage them to come join the game with their friends.
Target Market(s)
school students, teenagers, college girls
competition starts on 19th July 2013, and ends 30th Oct. 2013
@GLACIO FROZEN YOGHURT MARLOW PLAZA EAST ( next to Tandy's)

```html
<!DOCTYPE html>
<html lang="en">
<head>
<meta charset="utf-8">
<title>Best Glacio – Flyer</title>
<link rel="stylesheet" href="https://fonts.googleapis.com/css2?family=Yellowtail&family=Jost:wght@300;400&family=Oswald:wght@300;400&display=swap">
<style>
  :root {
    --paper: #ffffff;
    --ink: #111111;
    --magenta: #e6007e;
    --pink-soft: #e8a0b8;
    --pink-mid: #e45b9c;
    --charcoal: #231f20;
    --hairline-red: #e0001a;
    --hairline-grey: #9a9a9a;
    --photo-tone-a: #8d9188;
    --photo-tone-b: #3a3a3c;
    --white: #ffffff;
  }
  * { margin: 0; padding: 0; box-sizing: border-box; }
  html, body { width: 1200px; height: 835px; overflow: hidden; background: var(--paper); }
  body { position: relative; font-family: "Jost", "Futura", sans-serif; color: var(--ink); }

  .panel-label {
    position: absolute; top: 34px; font-size: 24px; font-weight: 400; text-align: center; width: 200px;
  }
  .panel-label--cover { left: 218px; }
  .panel-label--back { left: 755px; }

  /* Cover */
  .cover {
    position: absolute; left: 110px; top: 95px; width: 460px; height: 676px; overflow: hidden;
    background: linear-gradient(160deg, var(--magenta) 0%, var(--pink-mid) 30%, var(--pink-soft) 55%, var(--pink-mid) 78%, var(--magenta) 100%);
  }
  .cover__facets { position: absolute; inset: 0; }
  .cover__trim {
    position: absolute; left: 15px; top: 13px; right: 14px; bottom: 13px; border: 1px solid var(--ink);
  }
  .cover__title {
    position: absolute; left: 0; width: 100%; font-family: "Yellowtail", cursive; color: var(--white);
    font-size: 148px; line-height: 1; text-align: center;
  }
  .cover__title--first { top: 52px; left: -20px; }
  .cover__title--second { top: 190px; left: 8px; }
  .cover__prize {
    position: absolute; top: 330px; left: 0; width: 100%; text-align: center; color: var(--white);
    font-size: 25px; line-height: 29px; font-weight: 400;
  }
  .cover__page {
    position: absolute; top: 436px; left: 0; width: 100%; text-align: center; color: var(--white);
    font-family: "Yellowtail", cursive; font-size: 40px; line-height: 1;
  }
  .cover__rules {
    position: absolute; top: 500px; left: 0; width: 100%; text-align: center; color: var(--white);
    font-family: "Oswald", sans-serif; font-weight: 400; font-size: 18px; line-height: 29px; letter-spacing: 1.6px;
  }
  .cover__details {
    position: absolute; top: 600px; left: 0; width: 100%; text-align: center; color: var(--white);
    font-family: "Oswald", sans-serif; font-weight: 400; font-size: 13px; line-height: 20px; letter-spacing: 1px;
  }

  /* Back */
  .back {
    position: absolute; left: 642px; top: 95px; width: 459px; height: 676px; background: var(--charcoal);
    border: 1px solid var(--hairline-red);
  }
  .back__trim {
    position: absolute; left: 13px; top: 12px; right: 13px; bottom: 13px; border: 1px solid var(--hairline-grey);
  }
  .back__web {
    position: absolute; left: 264px; top: 98px; color: var(--white);
    font-family: "Oswald", sans-serif; font-weight: 400; font-size: 19px; letter-spacing: 2px;
  }
  .store-photo {
    position: absolute; border-radius: 50%; border: 8px solid var(--magenta);
    background: linear-gradient(180deg, var(--photo-tone-a) 0%, #b9bbb4 35%, var(--photo-tone-b) 70%, #cfcac2 100%);
  }
  .store-photo--small { left: 55px; top: 74px; width: 136px; height: 164px; width: 136px; height: 136px; }
  .store-photo--large { left: 208px; top: 213px; width: 214px; height: 214px; }
  .wordmark {
    position: absolute; left: 54px; top: 430px; width: 230px; color: var(--white);
    font-family: "Oswald", sans-serif; font-weight: 300; text-align: center;
  }
  .wordmark__name { display: block; font-size: 118px; line-height: 1; letter-spacing: 4px; }
  .wordmark__tag { display: block; font-size: 19px; letter-spacing: 3px; margin-top: 6px; }
</style>
</head>
<body>
  <div class="panel-label panel-label--cover">cover</div>
  <div class="panel-label panel-label--back">back</div>

  <section class="cover">
    <svg class="cover__facets" width="460" height="676" viewBox="0 0 460 676" aria-hidden="true">
      <polygon points="0,0 460,0 0,260" fill="#e6007e" opacity="0.25"/>
      <polygon points="290,290 460,440 460,676 250,676" fill="#e6007e" opacity="0.22"/>
      <polygon points="290,290 200,676 0,676 0,560" fill="#f2b3c9" opacity="0.25"/>
      <polygon points="0,560 0,676 120,676" fill="#e6007e" opacity="0.35"/>
    </svg>
    <div class="cover__trim"></div>
    <h1 class="cover__title cover__title--first">Best</h1>
    <h1 class="cover__title cover__title--second">Glacio</h1>
    <p class="cover__prize">Total prize up to $2,500 and<br>also get the chance to win a Tabula2<br>with custom glacio vinyl cover!</p>
    <p class="cover__page">chatterbox.com/Glacio</p>
    <p class="cover__rules">POST YOUR YOGHURT CREATION ON GLACIO CHAT-<br>TERBOX AND TAG #BESTGLACIO, WHO'S FROZEN<br>YOGHURT GETS THE MOST VOTE WIN THE GAME</p>
    <p class="cover__details">FOR MORE DETAILS<br>CHATTERBOX.COM/GLACIO</p>
  </section>

  <section class="back">
    <div class="back__trim"></div>
    <div class="store-photo store-photo--small" role="img" aria-label="Photo of the Glacio frozen yoghurt counter inside the shopping plaza"></div>
    <p class="back__web">GLACIOFY.COM</p>
    <div class="store-photo store-photo--large" role="img" aria-label="Photo of the Glacio store front and serving counter"></div>
    <div class="wordmark">
      <span class="wordmark__name">GLACIO</span>
      <span class="wordmark__tag">FROZEN YOGHURT</span>
    </div>
  </section>
</body>
</html>
```